Ridgeline Stick Works
Custom Wood Bats
guaranteed please...
For some reason, my numbers aren't showing up, but for the ones I rated, could you put the rest of the stationary with the cards? Looks great you all. Thanks!
increase the price please.....
#3, I like that. Can you make the seams red on the front of the ball or will the address not show up if you do?
Can you combine 7 & 8
Hi - so it is ok to alter the logo colors on the logo itself?
I would like to see some different colors. Maybe a navy blue print on the logo and then in the red part. Leave the ball white with red stitches. Look forward to seeing your interpretations.
Just uploaded it. My name doesn't have a "c" in it. Could you also put "Ridgeline Stick Works" somewhere on the front of the card? Also, I'm not a big fan of the all caps. Thanks for your design.
can you upload the original logo,please?

```html
<!DOCTYPE html>
<html lang="en">
<head>
<meta charset="utf-8">
<title>Ridgeline Stick Works – Business Card</title>
<link href="https://fonts.googleapis.com/css2?family=Alegreya+Sans:ital,wght@0,400;0,700;1,400;1,700&display=swap" rel="stylesheet">
<style>
  :root {
    --stage: #e6e6e6;
    --label: #555555;
    --red: #e8212b;
    --red-tint: #f7c9cb;
    --navy: #233f8c;
    --navy-tint: #c9d2ea;
    --white: #ffffff;
  }
  * { margin: 0; padding: 0; box-sizing: border-box; }
  html, body { width: 1200px; height: 897px; overflow: hidden; }
  body {
    background: var(--stage);
    font-family: "Alegreya Sans", sans-serif;
    position: relative;
  }
  .side-label {
    position: absolute;
    top: 22px;
    width: 430px;
    text-align: center;
    font-size: 22px;
    color: var(--label);
  }
  .side-label--front { left: 137px; }
  .side-label--back { left: 638px; }

  .card {
    position: absolute;
    top: 91px;
    width: 430px;
    height: 732px;
    overflow: hidden;
  }
  .card--front { left: 137px; background: var(--white); }
  .card--back { left: 638px; background: var(--navy); }
  .card__art { position: absolute; inset: 0; }

  .wordmark {
    position: absolute;
    top: 90px;
    left: 0;
    width: 430px;
    display: flex;
    align-items: center;
    justify-content: center;
    gap: 14px;
    font-weight: 700;
    font-size: 38px;
    line-height: 1.0;
    text-align: center;
  }
  .wordmark__dot {
    width: 32px; height: 32px; border-radius: 50%;
    flex: none;
  }
  .card--front .wordmark { color: var(--red); }
  .card--front .wordmark__dot { background: var(--red); }
  .card--back .wordmark { color: var(--white); }
  .card--back .wordmark__dot { background: var(--white); }

  .contact {
    position: absolute;
    left: 77px;
    top: 208px;
    color: var(--red);
    font-size: 18px;
    line-height: 26px;
  }
  .contact__phone { margin-top: 18px; font-weight: 700; }
  .contact__web { font-weight: 700; }

  .person {
    position: absolute;
    left: 53px;
    top: 574px;
    color: var(--white);
  }
  .person__name { font-size: 34px; font-weight: 700; line-height: 38px; }
  .person__title { font-size: 21px; font-style: italic; line-height: 28px; }
  .person__email { font-size: 19px; line-height: 30px; }

  .tagline {
    position: absolute;
    top: 330px;
    width: 430px;
    text-align: center;
    color: var(--white);
    font-size: 30px;
    font-style: italic;
  }
  .back-web {
    position: absolute;
    left: 101px;
    top: 640px;
    color: var(--navy);
    font-size: 20px;
  }
</style>
</head>
<body>
  <div class="side-label side-label--front">front</div>
  <div class="side-label side-label--back">back</div>

  <section class="card card--front">
    <svg class="card__art" width="430" height="732" viewBox="0 0 430 732">
      <path d="M21 557 V49 Q21 19 51 19 H379 Q409 19 409 49 V557" fill="none" stroke="var(--red)" stroke-width="4"/>
      <path d="M38 557 V54 Q38 36 56 36 H374 Q392 36 392 54 V557" fill="none" stroke="var(--red)" stroke-width="3"/>
      <rect x="0" y="557" width="430" height="175" fill="var(--red)"/>
      <rect x="293" y="519" width="104" height="128" fill="var(--red-tint)" role="img" aria-label="Home plate emblem with crossed bats"/>
    </svg>
    <div class="wordmark"><span class="wordmark__dot"></span><span>Ridgeline<br>Stick Works</span></div>
    <div class="contact">
      <div>P.O. Box 412</div>
      <div>Maple Hill, NC 28455</div>
      <div class="contact__phone">704.555.0182</div>
      <div class="contact__web">www.ridgelinesticks.com</div>
    </div>
    <div class="person">
      <div class="person__name">Dale Porter</div>
      <div class="person__title">Owner</div>
      <div class="person__email">dale@ridgelinesticks.com</div>
    </div>
  </section>

  <section class="card card--back">
    <svg class="card__art" width="430" height="732" viewBox="0 0 430 732">
      <path d="M21 557 V49 Q21 19 51 19 H379 Q409 19 409 49 V557" fill="none" stroke="var(--white)" stroke-width="4"/>
      <path d="M38 557 V54 Q38 36 56 36 H374 Q392 36 392 54 V557" fill="none" stroke="var(--white)" stroke-width="3"/>
      <rect x="0" y="557" width="430" height="175" fill="var(--white)"/>
      <rect x="293" y="519" width="104" height="128" fill="var(--navy-tint)" role="img" aria-label="Home plate emblem with crossed bats"/>
    </svg>
    <div class="wordmark"><span class="wordmark__dot"></span><span>Ridgeline<br>Stick Works</span></div>
    <div class="tagline">Custom Wood Bats</div>
    <div class="back-web">www.ridgelinesticks.com</div>
  </section>
</body>
</html>
```